K7 clearline

We are a glazing company specializing in frameless glass .
I would like the business cards in black with the logo taking up the most part of the front added with " frameless glass specialist's " below it.
On the back side I would like a list of what we do :
• shower screens
• glass balustrade / pool fencing
• mirrors
•office partitions
• sky lights
•shop fronts
•splash backs
Also include this information :
📧 - marcus@k7clearline.com
📞Marcus - 0412967528
📞 Colin - 0457 213 684
Updates
To all designs already posted can you include on the back of the card in the services part -
•splash backs
Target Market(s)
High end builders
Industry/Entity Type
Glazing
Contact Information for Business Card
On the back side I would like a list of what we do : • shower screens • glass balustrade / pool fencing • mirrors •office partitions • sky lights •shop fronts Also include this information : 📧 - marcus@k7clearline.com 📞Marcus - 0412967528 📞 Colin - 0457 213 684
Colors
Designer to choose colors to be used in the design.
Look and feel
Each slider illustrates characteristics of the customer's brand and the style your logo design should communicate.

```html
<!DOCTYPE html>
<html lang="en">
<head>
<meta charset="utf-8">
<title>K7 clearline – Business Card</title>
<link href="https://fonts.googleapis.com/css2?family=Montserrat:wght@300;400;500;600;700&display=swap" rel="stylesheet">
<style>
  :root {
    --backdrop: #5e5040;
    --card: #000000;
    --teal: #3bbfa6;
    --teal-deep: #1f9fae;
    --white: #ffffff;
    --text-dark: #111111;
    --divider-grey: #8a8a8a;
  }
  * { margin: 0; padding: 0; box-sizing: border-box; }
  html, body {
    width: 900px; height: 1200px; overflow: hidden;
    background: var(--backdrop);
    font-family: "Montserrat", sans-serif;
  }
  .canvas { position: relative; width: 900px; height: 1200px; }

  .card {
    position: absolute; left: 68px; width: 758px; height: 442px;
    background: var(--card); border-radius: 30px; overflow: hidden;
    box-shadow: 0 8px 22px rgba(0,0,0,0.45);
  }
  .card--front { top: 132px; }
  .card--back { top: 638px; }

  .identity { position: absolute; width: 290px; text-align: center; }
  .card--front .identity { left: 70px; top: 150px; }
  .card--back .identity { left: 58px; top: 160px; }
  .brand {
    display: inline-flex; align-items: center; gap: 10px;
    color: var(--white); font-weight: 600; font-size: 34px; letter-spacing: 0.3px;
    white-space: nowrap;
  }
  .brand__square { width: 20px; height: 20px; background: var(--teal); flex: none; }
  .tagline {
    margin-top: 10px; color: var(--teal); font-weight: 600; font-size: 14px;
    letter-spacing: 1.5px; text-transform: uppercase; white-space: nowrap;
  }

  .divider { position: absolute; }
  .card--front .divider { left: 383px; top: 104px; height: 222px; width: 2px; background: var(--teal-deep); }
  .card--back .divider { left: 386px; top: 102px; height: 272px; width: 1px; background: var(--divider-grey); }

  .contact { position: absolute; left: 430px; top: 100px; color: var(--white); }
  .contact__name { color: var(--teal-deep); font-weight: 700; font-size: 26px; line-height: 32px; }
  .contact__role { font-size: 16px; margin-top: 2px; }
  .contact__address { font-size: 16px; line-height: 20px; margin-top: 24px; }
  .contact__list { list-style: none; margin-top: 14px; }
  .contact__list li { display: flex; align-items: center; font-size: 16px; height: 25px; }
  .contact__icon { width: 18px; height: 18px; margin-right: 14px; flex: none; }
  .contact__who, .contact__accent { color: var(--teal); }
  .contact__accent { font-weight: 600; }

  .footer-band { position: absolute; left: 0; bottom: 0; width: 758px; height: 34px; }
  .footer-url {
    position: absolute; right: 92px; bottom: 7px; color: var(--text-dark);
    font-size: 15px; font-weight: 500;
  }

  .services { position: absolute; left: 438px; top: 94px; color: var(--white); }
  .services__title {
    color: var(--teal-deep); font-weight: 400; font-size: 28px;
    padding: 0 4px 8px 2px; border-bottom: 1.5px solid var(--white); display: inline-block;
    width: 180px;
  }
  .services__list { list-style: none; margin-top: 20px; }
  .services__list li { position: relative; padding-left: 22px; font-size: 17px; height: 31px; line-height: 22px; }
  .services__list li::before {
    content: ""; position: absolute; left: 3px; top: 7px; width: 9px; height: 9px;
    border-radius: 50%; background: var(--teal);
  }
</style>
</head>
<body>
<div class="canvas">

  <section class="card card--front">
    <div class="identity">
      <div class="brand"><span class="brand__square"></span>K7 clearline</div>
      <div class="tagline">Frameless glass specialists</div>
    </div>
    <div class="divider"></div>

    <div class="contact">
      <div class="contact__name">Tomas Reeve</div>
      <div class="contact__role">Owner</div>
      <div class="contact__address">418 Harbor View Rd, #112<br>Lakemont, OH 43190</div>
      <ul class="contact__list">
        <li>
          <svg class="contact__icon" viewBox="0 0 20 20" aria-hidden="true"><path fill="#3bbfa6" d="M3 7c0-2 2-3 7-3s7 1 7 3v1h-3l-1-2H7L6 8H3z M5 10h10l1 6H4z"/><circle cx="10" cy="13" r="1.8" fill="#000"/></svg>
          0412967528&nbsp;<span class="contact__who">(Marcus)</span>
        </li>
        <li>
          <svg class="contact__icon" viewBox="0 0 20 20" aria-hidden="true"><rect x="5" y="1.5" width="10" height="17" rx="2" fill="none" stroke="#3bbfa6" stroke-width="1.8"/><circle cx="10" cy="15.5" r="1" fill="#3bbfa6"/></svg>
          0457 213 684&nbsp;<span class="contact__who">(Colin)</span>
        </li>
        <li>
          <svg class="contact__icon" viewBox="0 0 20 20" aria-hidden="true"><rect x="3" y="5.5" width="14" height="10" fill="#3bbfa6"/><path d="M3 5.5l7 5 7-5" fill="none" stroke="#000" stroke-width="1.3"/></svg>
          marcus@<span class="contact__accent">k7clearline</span>.com
        </li>
        <li>
          <svg class="contact__icon" viewBox="0 0 20 20" aria-hidden="true"><circle cx="10" cy="10" r="7.5" fill="#3bbfa6"/><path d="M6 6c2 1 3 3 2 5-1 1 0 3 1 4M12 4c0 2 1 3 3 3M13 11c1 1 1 3 0 4" fill="none" stroke="#000" stroke-width="1.2"/></svg>
          www.<span class="contact__accent">k7clearline</span>.com
        </li>
      </ul>
    </div>

    <svg class="footer-band" viewBox="0 0 758 34" aria-hidden="true">
      <polygon points="0,20 394,20 388,34 0,34" fill="#3bbfa6"/>
      <polygon points="416,2 758,2 758,34 386,34" fill="#ffffff"/>
    </svg>
    <div class="footer-url">www.k7clearline.com</div>
  </section>

  <section class="card card--back">
    <div class="identity">
      <div class="brand"><span class="brand__square"></span>K7 clearline</div>
    </div>
    <div class="divider"></div>

    <div class="services">
      <h2 class="services__title">Our services</h2>
      <ul class="services__list">
        <li>shower screens</li>
        <li>glass balustrade / pool fencing</li>
        <li>mirrors</li>
        <li>office partitions</li>
        <li>sky lights</li>
        <li>shop fronts</li>
        <li>splash backs</li>
      </ul>
    </div>
  </section>

</div>
</body>
</html>
```